Business Card Design Project

1. Show the company logo.
2. Only company email ID and website address to be shown (office@tikhayavolna.fm , www.tikhayavolna.fm).
3. Logo to be provided by us, 2 designs just in case. The logo is made with ' Yasnaya Afisha' text, need to be edited so that it shows 'Yasnaya Afisha' instead .
4. Single sided business card, portrait or landscape is not a problem; back side to be filled with colors or a design that matches the logo the best.
5. Logo is to be embossed.
6. We're looking at an English and Russian version.
7. any other better idea is always welcomed.

```html
<!DOCTYPE html>
<html lang="en">
<head>
<meta charset="utf-8">
<title>Yasnaya Afisha — Business Card</title>
<link rel="stylesheet" href="https://fonts.googleapis.com/css2?family=Open+Sans:wght@400;700;800&display=swap">
<style>
  :root {
    --bg: #e6e7e9;
    --navy-deep: #0b2a63;
    --navy: #163f8c;
    --navy-light: #1f56ab;
    --yellow: #f7b500;
    --paper: #ffffff;
    --ink: #3a3a3a;
  }
  * { box-sizing: border-box; margin: 0; padding: 0; }
  html, body {
    width: 1200px; height: 900px; overflow: hidden;
    background: radial-gradient(ellipse at 60% 40%, #f7f7f8 0%, var(--bg) 75%);
    font-family: "Open Sans", Arial, sans-serif;
  }
  .canvas {
    position: relative; width: 1200px; height: 900px;
    display: flex; align-items: center; justify-content: center; gap: 60px;
  }
  .card {
    position: relative; width: 520px; height: 300px; overflow: hidden;
    box-shadow: 0 10px 30px rgba(0,0,0,.18);
  }
  /* Back side */
  .card--back {
    background: radial-gradient(circle at 38% 55%, var(--navy-light) 0%, var(--navy) 40%, var(--navy-deep) 100%);
    display: flex; align-items: center; justify-content: center;
  }
  .brand { display: flex; align-items: center; gap: 18px; }
  .brand__dot {
    flex: none; width: 64px; height: 64px; border-radius: 50%; background: var(--yellow);
  }
  .brand__name {
    color: var(--paper); font-weight: 700; font-size: 32px; letter-spacing: .5px;
    white-space: nowrap;
  }
  /* Front side */
  .card--front { background: var(--paper); }
  .front__brand {
    position: absolute; top: 34px; left: 34px; gap: 10px;
  }
  .front__brand .brand__dot { width: 30px; height: 30px; background: var(--navy); }
  .front__brand .brand__name { color: var(--navy); font-size: 17px; }
  .contact { position: absolute; right: 0; top: 150px; text-align right; }
  .contact { text-align: right; }
  .contact__web {
    display: block; color: var(--ink); font-weight: 800; font-size: 27px;
    padding-right: 28px; margin-bottom: 8px; white-space: nowrap;
  }
  .contact__mail {
    display: inline-block; background: var(--yellow); color: var(--paper);
    font-weight: 800; font-size: 27px; padding: 4px 28px 6px 26px; white-space: nowrap;
  }
</style>
</head>
<body>
  <main class="canvas">
    <section class="card card--back" aria-label="Card back">
      <div class="brand">
        <span class="brand__dot"></span>
        <span class="brand__name">Yasnaya Afisha</span>
      </div>
    </section>
    <section class="card card--front" aria-label="Card front">
      <div class="front__brand brand">
        <span class="brand__dot"></span>
        <span class="brand__name">Yasnaya Afisha</span>
      </div>
      <div class="contact">
        <span class="contact__web">www.tikhayavolna.fm</span>
        <span class="contact__mail">office@tikhayavolna.fm</span>
      </div>
    </section>
  </main>
</body>
</html>
```